Premium Nail Dip Powder Label Design

We need a label design for a 2 ounce jar in which we will be selling our new product line of dip powder to nail salons. For reference, please see competitors' products that are currently selling in the market. The label size is 16cm long by 2.5cm wide. We have a logo design that is attached - the "drop" should be in shiny gold (metallic). This label will wrap around the round jar and the first half will be the "front" and the second half will be the "back". Please see the attached writing that will be required for the second half, or "back" part of the label.

Target Market(s)

Retail Nail Salons in the US

Font styles to use
Sans Serif

Colors

Designer to choose colors to be used in the design.

Requirements
Must have
• "RVT" logo with the "drop" in shiny/metallic gold to match the shiny gold lid that we will have for it. The words "Premium Dip Powder". The size "2 oz". The wording for the second half, or "back" part of the label attached should be in black color with the size adjusted to fit the label size.
Nice to have
• different designs of fonts and sizes and colors for "Premium Dip Powder" which should be on the "front" of the label under our logo.

```html
<!DOCTYPE html>
<html lang="en">
<head>
<meta charset="utf-8">
<title>RVT Premium Dip Powder Label</title>
<link href="https://fonts.googleapis.com/css2?family=Montserrat:wght@300;700&family=Arimo:wght@400;700&display=swap" rel="stylesheet">
<style>
  :root {
    --page-bg: #ffffff;
    --purple-deep: #7a1fa8;
    --purple-mid: #a447d6;
    --purple-glow: #d77ef2;
    --label-ink: #f4e8f8;
    --gold: #c9a24a;
    --back-ink: #111111;
  }
  html, body {
    margin: 0;
    padding: 0;
    width: 1199px;
    height: 1200px;
    overflow: hidden;
    background: var(--page-bg);
  }
  .canvas {
    position: relative;
    width: 1199px;
    height: 1200px;
  }
  .label-panel {
    position: absolute;
    top: 504px;
    width: 482px;
    height: 320px;
    border-radius: 6px;
    background: linear-gradient(90deg,
      var(--purple-mid) 0%,
      var(--purple-glow) 10%,
      var(--purple-mid) 30%,
      #b65ad9 60%,
      var(--purple-mid) 80%,
      var(--purple-deep) 100%);
    overflow: hidden;
  }
  .label-front { left: 62px; }
  .label-back { left: 662px; }

  .brand {
    position: absolute;
    left: 0;
    right: 0;
    top: 52px;
    text-align: center;
    font-family: "Montserrat", sans-serif;
    font-weight: 700;
    font-size: 124px;
    line-height: 1;
    letter-spacing: -2px;
    color: var(--label-ink);
  }
  .brand-dot {
    position: absolute;
    left: 388px;
    top: 64px;
    width: 24px;
    height: 24px;
    border-radius: 50%;
    background: var(--gold);
  }
  .product-name {
    position: absolute;
    left: 0;
    right: 0;
    top: 172px;
    text-align: center;
    font-family: "Montserrat", sans-serif;
    font-weight: 300;
    font-size: 35px;
    line-height: 38px;
    letter-spacing: 2px;
    color: var(--label-ink);
  }
  .net-weight {
    position: absolute;
    left: 0;
    right: 0;
    top: 264px;
    text-align: center;
    font-family: "Arimo", sans-serif;
    font-weight: 400;
    font-size: 14px;
    color: var(--label-ink);
  }

  .back-copy {
    position: absolute;
    left: 76px;
    top: 34px;
    width: 360px;
    font-family: "Arimo", sans-serif;
    font-weight: 700;
    font-size: 13px;
    line-height: 17px;
    color: var(--back-ink);
  }
  .back-copy p { margin: 0 0 16px; }
  .back-copy .caution { margin-bottom: 21px; }
  .back-copy .heading { display: block; }
  .maker {
    position: absolute;
    left: 245px;
    top: 232px;
    font-family: "Arimo", sans-serif;
    font-weight: 700;
    font-size: 10.5px;
    line-height: 13.5px;
    color: var(--back-ink);
  }
</style>
</head>
<body>
<main class="canvas">
  <section class="label-panel label-front" aria-label="Label front">
    <div class="brand">RVT</div>
    <span class="brand-dot" aria-hidden="true"></span>
    <div class="product-name">PREMIUM<br>DIP POWDER</div>
    <div class="net-weight">Net Wt. 2 oz</div>
  </section>

  <section class="label-panel label-back" aria-label="Label back">
    <div class="back-copy">
      <p>For Use By Nail Professionals Only</p>
      <p class="caution">CAUTION: KEEP OUT OF REACH OF CHILDREN.<br>
        Keep away from heat, humidity and sunlight.<br>
        Discontinue use if sensitivity or irritation occurs.</p>
      <p><span class="heading">INGREDIENTS:</span>
        Polyethylmethacrylate, Acrylates Copolymer, Benzoyl Peroxide and PEG-12 Dimethicone. May also contain various coloring agents and glitters.</p>
    </div>
    <div class="maker">Manufactured Exclusively For:<br>
      Blue Harbor Trading, Inc., USA<br>
      www.blueharbortrading.com</div>
  </section>
</main>
</body>
</html>
```